Thornbury Lettings Managment Ltd website

Need a website To inform people/clients of the services we provide. 5 pages total with a local feel. Bristol, UK. I have logo artwork already is like the look based on
incorporate the artwork attached for theme, feel and colours fonts info etc

To best describe the business have a brief look at www.fernwickhomes.example.co.uk which is a local firm offering the same services. This is for your ref only and not to be copied.

Target Market(s)

Property Investors/Landlords

Coding

Coded - Design and coding required

Number of Pages Required

5+ page

Colors
0392cd
f68d4d

Requirements
Must have
• local feel. Possibly using some local architecture or historic landmarks etc. This is fexible.
• most also be mobile device compatible
Nice to have
• the membership logos - files attached: KTB, DWF, GMV and safehold-example.co.uk

```html
<!DOCTYPE html>
<html lang="en">
<head>
<meta charset="utf-8">
<title>Thornbury Lettings Managment Ltd</title>
<link href="https://fonts.googleapis.com/css2?family=Asap:wght@400;500;600&family=Open+Sans:wght@400;600;700&display=swap" rel="stylesheet">
<style>
:root{
  --navy:#1d3b53;
  --blue:#0392cd;
  --label:#0c5a9a;
  --orange:#f68d4d;
  --orange-dk:#ee8a1f;
  --text:#555f66;
  --light:#eef1f3;
  --footer:#1b2735;
  --footer-dk:#121b26;
  --white:#ffffff;
}
*{box-sizing:border-box;margin:0;padding:0}
html,body{width:1200px;height:4369px;overflow:hidden}
body{font-family:"Open Sans",Arial,sans-serif;color:var(--text);background:var(--white);font-size:14px;line-height:1.6}
h1,h2,h3,.brand-name,.nav a{font-family:"Asap",Arial,sans-serif}
.wrap{width:1040px;margin:0 auto;position:relative}

/* header */
.site-header{height:93px;background:var(--white);display:flex;align-items:center;justify-content:space-between;padding:0 80px}
.brand{display:flex;align-items:center;gap:12px}
.brand-mark{width:44px;height:44px;background:var(--navy)}
.brand-name{font-size:24px;font-weight:600;color:var(--navy);line-height:1.1}
.nav{display:flex;gap:26px}
.nav a{font-size:17px;color:var(--navy);text-decoration:none}
.nav a.active{color:var(--orange-dk)}

/* hero */
.hero{height:621px;position:relative;background:linear-gradient(180deg,#4f9fd6 0%,#8cc2e8 35%,#c9c3b4 58%,#7a6e5a 72%,#6d8fa5 84%,#3d6d8f 100%);text-align:center;color:var(--white)}
.hero h1{padding-top:50px;font-size:58px;font-weight:500;letter-spacing:.5px}
.hero p{font-family:"Asap",sans-serif;font-size:24px;color:#10243a;margin-top:2px}

/* sections */
.section{position:relative;text-align:center}
.section h2{font-size:44px;font-weight:500;color:var(--navy)}
.intro{width:1010px;margin:22px auto 0;font-size:15px;line-height:1.65}
.about{height:591px;padding-top:46px}
.about-body{display:flex;justify-content:space-between;text-align:left;margin-top:40px;padding:0 80px}
.about-text{width:650px;font-size:13.5px}
.about-text .lead{color:var(--orange-dk);font-weight:700;font-size:15.5px;margin-bottom:18px}
.photo-grid{width:304px;display:grid;grid-template-columns:1fr 1fr;gap:4px}
.photo-grid div{height:158px}

.services{height:641px;padding-top:62px;background:linear-gradient(180deg,#dfe6ec,#eef2f5 60%,#e4eaef)}
.cards{display:flex;justify-content:space-between;padding:0 84px;margin-top:80px}
.card{width:330px;text-align:left}
.card-image{height:189px;border:8px solid var(--white);position:relative;box-shadow:0 2px 6px rgba(0,0,0,.12)}
.card-label{position:absolute;left:-8px;bottom:12px;width:272px;background:var(--label);color:var(--white);font-family:"Asap",sans-serif;font-weight:600;font-size:16px;padding:4px 12px}
.card p{font-size:12px;line-height:1.5;margin-top:24px;padding:0 4px}
.read-more{display:flex;align-items:center;gap:8px;margin-top:22px;font-size:12px;color:var(--orange-dk)}
.read-more span.dot{width:22px;height:22px;background:var(--navy);border-radius:50%}

.benefits{height:594px;padding-top:44px}
.benefits.tinted{background:var(--light);height:621px}
.benefit-body{display:flex;justify-content:space-between;text-align:left;padding:0 80px;margin-top:70px}
.benefit-photo{width:306px;height:320px;border:2px solid #d7dde1}
.benefit-list{width:665px}
.benefit-list h3{color:var(--orange-dk);font-size:22px;font-weight:600;margin-bottom:20px}
.benefit-list ul{list-style:none}
.benefit-list li{position:relative;padding-left:26px;font-size:13.5px;line-height:1.6;margin-bottom:24px}
.benefit-list li::before{content:"";position:absolute;left:2px;top:7px;width:9px;height:9px;border-radius:50%;background:var(--label)}

/* footer */
.site-footer{height:611px;background:linear-gradient(180deg,#22303f,var(--footer));color:var(--white);position:relative}
.partners{position:absolute;left:82px;top:64px;width:1037px;height:82px;background:var(--white);display:flex;align-items:center;justify-content:space-around}
.partners .badge{width:150px;height:46px;background:#d5dbe1}
.partners .sep{width:1px;height:50px;background:#c7ced4}
.footer-col h3{font-size:18px;font-weight:600;margin-bottom:22px}
.contact{position:absolute;left:82px;top:198px;width:330px}
.contact-row{display:flex;gap:14px;font-size:13px;margin-bottom:36px;align-items:flex-start}
.contact-row .k{color:var(--orange-dk);width:70px;display:flex;gap:8px;align-items:center}
.socials{display:flex;gap:10px;margin-top:20px}
.socials span{width:26px;height:26px;border-radius:50%;background:#e9a83e}
.contact-form{position:absolute;left:480px;top:198px;width:306px}
.field{height:38px;background:var(--white);margin-bottom:8px;font-size:11px;color:#888;padding:10px 8px}
.field.msg{height:84px}
.submit{height:38px;background:var(--orange-dk);text-align:center;font-size:14px;line-height:38px}
.footer-aside{position:absolute;left:903px;top:180px;width:218px;text-align:center}
.footer-aside .brand-name{color:#8fb0c8;font-size:26px;margin-bottom:20px}
.map{height:226px;background:linear-gradient(135deg,#dfe6dc,#cfd8cf);clip-path:polygon(50% 0,100% 35%,100% 100%,0 100%,0 35%)}
.map-link{font-size:12px;color:var(--orange-dk);margin-top:8px}
.copyright{position:absolute;left:0;bottom:0;width:100%;height:58px;background:var(--footer-dk);text-align:center;font-size:12px;color:#8894a0;line-height:58px}
</style>
</head>
<body>

<header class="site-header">
  <div class="brand"><span class="brand-mark"></span><span class="brand-name">Thornbury</span></div>
  <nav class="nav">
    <a class="active" href="#">Home</a><a href="#">About Thornbury</a><a href="#">What We Do</a><a href="#">Landlords</a><a href="#">Tenants</a><a href="#">Agencies</a><a href="#">Contacts</a>
  </nav>
</header>

<section class="hero" role="img" aria-label="Photo of modern waterfront apartment blocks above a river at dusk">
  <h1>Thornbury Estates Management</h1>
  <p>The Great Estates Management In Your Locality</p>
</section>

<section class="section about">
  <h2>About Thornbury</h2>
  <p class="intro">Lorem Ipsum is simply dummy text of the printing and typesetting industry. Lorem Ipsum has been that industry's standard dummy text ever since the 1500s. In vehicula, felis ac tincidunt congue, neque velit blandit risus, eu semper augue augue a arcu.</p>
  <div class="about-body">
    <div class="about-text">
      <p class="lead">Phasellus nec turpis mattis, porttitor lacus ut, gravida arcu. Phasellus bibendum semper eodiam dapibus in.</p>
      <p>Sed semper, nibh at porta commodo, eros dui efficitur risus, a elementum augue elit at erat. Suspendisse imperdiet ut nibh a condimentum. Suspendisse molestie sapien sit amet leo mattis hendrerit sit amet in leo.</p>
      <p>Vivamus gravida lectus purus. Donec sagittis hendrerit elit. Vivamus mollis, lectus ac tempor finibus, metus ex dapibus nunc, eget pellentesque felis quam eget ligula. Donec interdum non nunc nec feugiat. Etiam a erat pulvinar, luctus ex et, laoreet ante. Vivamus varius volutpat bibendum. Proin lobortis magna sed elit iaculis.</p>
      <p>Lorem ipsum dolor sit amet, consectetur adipiscing elit. Nunc convallis rutrum elit at venenatis. Donec vitae hendrerit nibh, quis imperdiet massa. In vehicula, felis ac tincidunt congue, neque velit blandit risus, eu semper augue a arcu.</p>
    </div>
    <div class="photo-grid">
      <div role="img" aria-label="Photo of a tall city building" style="background:linear-gradient(160deg,#9fb6c9,#6f5f52)"></div>
      <div role="img" aria-label="Photo of a historic street facade" style="background:linear-gradient(160deg,#b9a993,#5b5b60)"></div>
      <div role="img" aria-label="Photo of a waterfront with old warehouses" style="background:linear-gradient(160deg,#b5c8d6,#8a7658)"></div>
      <div role="img" aria-label="Photo of colourful harbourside houses" style="background:linear-gradient(160deg,#d0a47a,#6d7f8c)"></div>
    </div>
  </div>
</section>

<section class="section services">
  <h2>What We Do</h2>
  <p class="intro">Lorem Ipsum is simply dummy text of the printing and typesetting industry. Lorem Ipsum has been that industry's standard dummy text ever since the 1500s. In vehicula, felis ac tincidunt congue, neque velit blandit risus, eu semper augue augue a arcu.</p>
  <div class="cards">
    <article class="card">
      <div class="card-image" role="img" aria-label="Illustration of a house outline held in an open hand" style="background:linear-gradient(160deg,#1e6fb5,#6ab0e4)"><span class="card-label">Good With Management</span></div>
      <p>Donec egestas vitae mauris hendrerit ing euismod. Vestibulum vehicula vitae dum sodales interdum. Etiam a erat pulvinar, luctus ex et, laoreet ante. Lorem ipsum dolor sit amet, consectetur adipiscing elit. Nulla dapibus nisl ac urna accumsan porttitor.</p>
      <div class="read-more"><span class="dot"></span>Read More...</div>
    </article>
    <article class="card">
      <div class="card-image" role="img" aria-label="Photo of stacked coins growing in rows" style="background:linear-gradient(160deg,#c9b78e,#7b6a45)"><span class="card-label">Good With Finance</span></div>
      <p>Donec egestas vitae mauris hendrerit ing euismod. Vestibulum vehicula vitae dum sodales interdum. Etiam a erat pulvinar, luctus ex et, laoreet ante. Lorem ipsum dolor sit amet, consectetur adipiscing elit. Nulla dapibus nisl ac urna accumsan porttitor.</p>
      <div class="read-more"><span class="dot"></span>Read More...</div>
    </article>
    <article class="card">
      <div class="card-image" role="img" aria-label="Photo of a detached family house under blue sky" style="background:linear-gradient(180deg,#5d9bd6,#a7845e 70%,#5f7a3d)"><span class="card-label">Good With Maintenance</span></div>
      <p>Donec egestas vitae mauris hendrerit ing euismod. Vestibulum vehicula vitae dum sodales interdum. Etiam a erat pulvinar, luctus ex et, laoreet ante. Lorem ipsum dolor sit amet, consectetur adipiscing elit. Nulla dapibus nisl ac urna accumsan porttitor.</p>
      <div class="read-more"><span class="dot"></span>Read More...</div>
    </article>
  </div>
</section>

<section class="section benefits">
  <h2>Landlords</h2>
  <p class="intro">Lorem Ipsum is simply dummy text of the printing and typesetting industry. Lorem Ipsum has been that industry's standard dummy text ever since the 1500s. In vehicula, felis ac tincidunt congue, neque velit blandit risus, eu semper augue augue a arcu.</p>
  <div class="benefit-body">
    <div class="benefit-photo" role="img" aria-label="Photo of a landlord handing house keys to a couple at a front door" style="background:linear-gradient(150deg,#c8b9a2,#8d7a64 60%,#6f8aa0)"></div>
    <div class="benefit-list">
      <h3>We give the following benefits to landlords:</h3>
      <ul>
        <li>Lorem ipsum dolor sit amet, consectetur adipiscing elit. Nunc convallis rutrum elit at venenatis. Donec vitae hendrerit nibh, quis imperdiet massa. Nam in nulla lacinia.</li>
        <li>Lorem ipsum dolor sit amet, consectetur adipiscing elit. Nunc convallis rutrum elit at venenatis. Donec vitae hendrerit nibh, quis imperdiet massa. Nam in nulla lacinia.</li>
        <li>Lorem ipsum dolor sit amet, consectetur adipiscing elit. Nunc convallis rutrum elit at venenatis. Donec vitae hendrerit nibh, quis imperdiet massa. Nam in nulla lacinia.</li>
        <li>Lorem ipsum dolor sit amet, consectetur adipiscing elit. Nunc convallis rutrum elit at venenatis. Donec vitae hendrerit nibh, quis imperdiet massa. Nam in nulla lacinia.</li>
      </ul>
    </div>
  </div>
</section>

<section class="section benefits tinted">
  <h2>Tenants</h2>
  <p class="intro">Lorem Ipsum is simply dummy text of the printing and typesetting industry. Lorem Ipsum has been that industry's standard dummy text ever since the 1500s. In vehicula, felis ac tincidunt congue, neque velit blandit risus, eu semper augue augue a arcu.</p>
  <div class="benefit-body">
    <div class="benefit-list">
      <h3>We give the following benefits to tenants:</h3>
      <ul>
        <li>Lorem ipsum dolor sit amet, consectetur adipiscing elit. Nunc convallis rutrum elit at venenatis. Donec vitae hendrerit nibh, quis imperdiet massa. Nam in nulla lacinia.</li>
        <li>Lorem ipsum dolor sit amet, consectetur adipiscing elit. Nunc convallis rutrum elit at venenatis. Donec vitae hendrerit nibh, quis imperdiet massa. Nam in nulla lacinia.</li>
        <li>Lorem ipsum dolor sit amet, consectetur adipiscing elit. Nunc convallis rutrum elit at venenatis. Donec vitae hendrerit nibh, quis imperdiet massa. Nam in nulla lacinia.</li>
        <li>Lorem ipsum dolor sit amet, consectetur adipiscing elit. Nunc convallis rutrum elit at venenatis. Donec vitae hendrerit nibh, quis imperdiet massa. Nam in nulla lacinia.</li>
      </ul>
    </div>
    <div class="benefit-photo" role="img" aria-label="Photo of a smiling couple in their new home" style="background:linear-gradient(150deg,#9aa5ad,#c58a7f 55%,#3c4a58)"></div>
  </div>
</section>

<section class="section benefits">
  <h2>Agencies</h2>
  <p class="intro">Lorem Ipsum is simply dummy text of the printing and typesetting industry. Lorem Ipsum has been that industry's standard dummy text ever since the 1500s. In vehicula, felis ac tincidunt congue, neque velit blandit risus, eu semper augue augue a arcu.</p>
  <div class="benefit-body">
    <div class="benefit-photo" role="img" aria-label="Photo of a handshake over a small model house" style="background:linear-gradient(150deg,#f2f2f2,#c94040 45%,#8b6b55)"></div>
    <div class="benefit-list">
      <h3>We give the following benefits to landlords:</h3>
      <ul>
        <li>Lorem ipsum dolor sit amet, consectetur adipiscing elit. Nunc convallis rutrum elit at venenatis. Donec vitae hendrerit nibh, quis imperdiet massa. Nam in nulla lacinia.</li>
        <li>Lorem ipsum dolor sit amet, consectetur adipiscing elit. Nunc convallis rutrum elit at venenatis. Donec vitae hendrerit nibh, quis imperdiet massa. Nam in nulla lacinia.</li>
        <li>Lorem ipsum dolor sit amet, consectetur adipiscing elit. Nunc convallis rutrum elit at venenatis. Donec vitae hendrerit nibh, quis imperdiet massa. Nam in nulla lacinia.</li>
        <li>Lorem ipsum dolor sit amet, consectetur adipiscing elit. Nunc convallis rutrum elit at venenatis. Donec vitae hendrerit nibh, quis imperdiet massa. Nam in nulla lacinia.</li>
      </ul>
    </div>
  </div>
</section>

<footer class="site-footer">
  <div class="partners" aria-label="Membership badges">
    <span class="badge"></span><span class="sep"></span>
    <span class="badge"></span><span class="sep"></span>
    <span class="badge"></span><span class="sep"></span>
    <span class="badge"></span>
  </div>

  <div class="footer-col contact">
    <h3>Contact Details</h3>
    <div class="contact-row"><span class="k"><svg width="12" height="16" viewBox="0 0 12 16"><path d="M6 0a6 6 0 0 0-6 6c0 4.5 6 10 6 10s6-5.5 6-10a6 6 0 0 0-6-6zm0 8.5A2.5 2.5 0 1 1 6 3.5a2.5 2.5 0 0 1 0 5z" fill="#fff"/></svg>Address:</span><span>14 Harbour Row, Redcliffe<br>Bristol BS1 6XX</span></div>
    <div class="contact-row"><span class="k"><svg width="14" height="14" viewBox="0 0 14 14"><path d="M3 0l2 3-1.5 2a8 8 0 0 0 5.5 5.5L11 9l3 2-1.5 3C6 14 0 8 0 1.5z" fill="#fff"/></svg>Phone:</span><span>+44 (0)117 496 0123</span></div>
    <div class="contact-row"><span class="k"><svg width="14" height="10" viewBox="0 0 14 10"><rect width="14" height="10" fill="#fff"/><path d="M0 0l7 6 7-6" stroke="#1b2735" fill="none"/></svg>Email:</span><span>hello@thornbury.example</span></div>
    <div class="socials"><span></span><span></span><span></span><span></span></div>
  </div>

  <div class="footer-col contact-form">
    <h3>Contact Us</h3>
    <div class="field">Name:</div>
    <div class="field">Email:</div>
    <div class="field">Phone:</div>
    <div class="field msg">Message:</div>
    <div class="submit">Submit</div>
  </div>

  <div class="footer-aside">
    <div class="brand-name">Thornbury</div>
    <div class="map" role="img" aria-label="Street map of the office location"></div>
    <div class="map-link">View Larger Map ›</div>
  </div>

  <div class="copyright">Copyright @thornbury.example. All rights reserved.</div>
</footer>

</body>
</html>
```